finlo-welt.de
Zielgruppe
Alle die kein Geld haben :-)
Aufgabenstellung
Unter finlo-welt.de sollen Informationen rund um Kredite, Kreditkarten, Bonvia usw. entstehen. Diese werden dann unter Subdomains wir konto.finlo-welt.de oder kreditkarte.finlo-welt.de laufen. Die Domain finlo-welt.de soll die Hauptdomain werden wofür ein Logo und ein Layout benötigt wird. Auf den einzelnen Seiten sollen später Reporte verkauft werden und relativ viel mit Plunko Werbung gearbeitet werden. Hier ein paar Beipspiele www.zahlwerk-mohnel.biz, www.lumvesta88.de, www.tanne-blau-heft.de, www.nordlicht-mappe-brief.de
Die genannten Seiten sind keine Meisterleistung in Design und sollen nur in etwa Inhalte und die Einbindung von Plunko Adbox wieder geben. Menüpunkte sind immer gleich und werden sein mit den Untertiteln wie bei www.zahlwerk-mohnel.biz.

```html
<!DOCTYPE html>
<html lang="de">
<head>
<meta charset="utf-8">
<title>finlo-welt.de</title>
<link rel="stylesheet" href="https://fonts.googleapis.com/css2?family=Noto+Sans:wght@400;700&family=Roboto+Condensed:wght@300;400;700&display=swap">
<style>
:root{
  --page:#eeeeee;
  --column:#f7f7f7;
  --side:#dcdcdc;
  --side-dark:#cfcfcf;
  --orange:#f39019;
  --link-blue:#1f4e8c;
  --nav-blue:#6a8db4;
  --text:#333;
  --muted:#555;
  --card:#e3e3e3;
  --card-text:#24457a;
  --head-gray:#6f6f6f;
  --pill:#dfe6ef;
  --arrow-box:#6c8fb8;
}
*{box-sizing:border-box;margin:0;padding:0}
html,body{width:1200px;height:1029px;overflow:hidden}
body{background:var(--page);font-family:"Noto Sans",Verdana,sans-serif;color:var(--text);position:relative}
a{color:inherit;text-decoration:none}
.column{position:absolute;left:27px;top:0;width:1135px;height:1029px;background:var(--column)}
.abs{position:absolute}
.logo{left:44px;top:34px;font-size:46px;font-weight:700;color:var(--orange);letter-spacing:-1px}
.topnav,.footnav{font-size:13px;color:var(--nav-blue);letter-spacing:.5px;word-spacing:4px}
.topnav{left:882px;top:68px}
.footnav{left:874px;top:960px}
.sidebar{left:40px;top:114px;width:265px;height:864px;background:linear-gradient(90deg,var(--side),#e6e6e6);box-shadow:2px 3px 5px rgba(0,0,0,.25)}
.side-item{position:absolute;left:32px;font-size:14px;line-height:17px;color:#444}
.side-item b{display:block;font-weight:400;color:#222;text-decoration:underline}
.side-item i{display:block;font-style:normal;color:var(--link-blue)}
.side-home{position:absolute;left:4px;top:18px;font-size:15px;color:#222;text-decoration:underline}
.sq{display:inline-block;width:17px;height:17px;background:#555;margin-right:9px;vertical-align:-3px;position:relative}
.sq:after{content:"";position:absolute;left:6px;top:4px;border-left:6px solid #fff;border-top:4.5px solid transparent;border-bottom:4.5px solid transparent}
.adhead{position:absolute;left:5px;width:250px;height:18px;font-size:12px;color:#555}
.adhead .nav{display:inline-block;width:17px;height:17px;background:#aaa;margin-right:2px}
.adhead .nav.on{background:#555}
.adhead span.lbl{position:absolute;right:25px;top:0}
.adhead span.lbl b{font-size:15px;font-weight:400;color:#777}
.hero{left:321px;top:112px;width:831px;height:205px;background:linear-gradient(90deg,#ececec 0%,#f4f4f4 40%,#e9ecef 100%)}
.hero-photo{position:absolute;right:0;top:0;width:420px;height:205px;background:linear-gradient(90deg,rgba(240,240,240,0),#dfe3e7 35%,#f0f2f4 100%)}
.hero-title{position:absolute;left:32px;top:16px;font-family:"Roboto Condensed",sans-serif;color:var(--orange);line-height:1}
.hero-title .big{font-size:40px;font-weight:400}
.hero-title .small{font-size:22px;font-weight:300;display:block;margin-top:2px}
.newsletter{position:absolute;left:18px;top:167px;width:210px;height:32px;background:#fff;border:1px solid #ddd;font-size:14px;color:#888;padding:6px 10px}
.newsletter .go{position:absolute;right:0;top:0;width:30px;height:30px;background:var(--arrow-box)}
.go:after{content:"";position:absolute;left:11px;top:8px;border-left:9px solid #fff;border-top:7px solid transparent;border-bottom:7px solid transparent}
.card{top:387px;width:390px;height:102px;background:linear-gradient(180deg,#e8e8e8,#dadada);box-shadow:2px 3px 5px rgba(0,0,0,.25)}
.card h2{position:absolute;left:12px;top:12px;font-family:"Roboto Condensed",sans-serif;font-weight:700;font-size:19px;color:var(--head-gray);letter-spacing:.3px}
.card p{position:absolute;left:12px;top:52px;width:310px;font-size:14px;line-height:18px;color:var(--card-text)}
.card .chev{position:absolute;right:12px;top:50px;width:44px;height:40px;background:#f2f2f2}
.intro{left:353px;top:546px;width:341px;font-size:14px;line-height:18px;color:#24457a;text-align:justify}
.intro h3{font-size:14px;font-weight:700;color:#1a2f66;margin-bottom:10px}
.intro p{margin-bottom:14px}
.teaser{position:absolute;left:353px;font-size:14px;line-height:18px;color:#24457a}
.teaser:before{content:"›";position:absolute;left:0;top:-1px;color:#333;font-size:18px}
.teaser span{display:block;padding-left:19px}
.more{left:357px;top:902px;font-size:14px;font-weight:700;color:#777}
.more .sq{margin-left:8px;margin-right:0}
.product{left:757px;top:609px;width:151px;height:148px;background:linear-gradient(135deg,#2f6fb6,#1e4f8e 60%,#8fa9c6);border-radius:6px}
.adhead2{left:922px;top:522px;width:195px}
.ad2{position:absolute;left:925px;font-size:14px;line-height:17px;color:#444}
.ad2 b{display:block;font-weight:400;color:#1a2f66;text-decoration:underline}
.ad2 i{display:block;font-style:normal;color:var(--link-blue)}
.pillbox{left:758px;top:808px;width:388px;height:104px;background:#fff}
.pill{position:absolute;left:5px;width:371px;height:31px;background:var(--pill);border-radius:8px;font-size:14px;color:#1a2f66;padding:6px 0 0 44px}
.pill .go{position:absolute;left:0;top:0;width:31px;height:31px;background:var(--arrow-box);border-radius:8px}
.pill .go:after{left:12px;top:9px;border-left:7px solid #fff;border-top:6px solid transparent;border-bottom:6px solid transparent}
</style>
</head>
<body>
<div class="column"></div>

<div class="abs logo">finlo-welt.de</div>
<nav class="abs topnav">HOME | LINK | LINK | LINK | LINK</nav>

<aside class="abs sidebar">
  <a class="side-home"><span class="sq"></span>Startseite</a>
  <div class="side-item" style="top:52px"><b>Angebote</b>Interessante Angebote<i>www.finlowelt.de/angebote</i></div>
  <div class="side-item" style="top:122px"><b>Reports</b>Inforeports auf einen Blick<i>www.finlowelt.de/reports</i></div>
  <div class="adhead" style="top:203px"><span class="nav"></span><span class="nav on"></span><span class="lbl"><b>Plunko</b>-Anzeigen</span></div>
  <div class="side-item" style="top:242px;left:30px"><b>Kostenloses Girokonto</b>mit 50 € Aktivitätsprämie.<br>Jetzt wechseln &amp; Girokonto<br>eröffnen!<i>www.kontovelo.de/girokonto</i></div>
  <div class="side-item" style="top:347px;left:30px"><b>Velmora Reisekarte</b>5% Rückvergütung beim<br>Reisen. Attraktive Guthaben-<br>verzinsung!<i>www.velmorabank.de</i></div>
  <div class="side-item" style="top:466px;left:30px"><b>Angebote</b>Interessante Angebote<i>www.finlowelt.de/angebote</i></div>
  <div class="side-item" style="top:536px;left:30px"><b>Reports</b>Inforeports auf einen Blick<i>www.finlowelt.de/reports</i></div>
  <div class="adhead" style="top:615px"><span class="nav"></span><span class="nav on"></span><span class="lbl"><b>Plunko</b>-Anzeigen</span></div>
  <div class="side-item" style="top:656px;left:30px"><b>NEU: Trevix Prepaidkarte</b>Exklusive Prepaid Karte<br>inkl. Konto, Geldversenden,<br>24Std Service<i>www.trevixkarte.com</i></div>
  <div class="side-item" style="top:762px;left:30px"><b>Kredit Karten ab 3,45%</b>Alle Kredite im Vergleich. Hier<br>gibts die niedrigsten Kredit<br>Zinsen<i>www.Tarifblick.de/Kredit</i></div>
</aside>

<section class="abs hero">
  <div class="hero-photo" role="img" aria-label="Foto: lächelnder Mann im hellen Hemd mit Laptop in heller Wohnung"></div>
  <div class="hero-title"><span class="big">WILLKOMMEN</span><span class="small">BEI FINLO-WELT</span></div>
  <div class="newsletter">Email für Newsletter<span class="go"></span></div>
</section>

<a class="abs card" style="left:341px">
  <h2>ONLINE-ANTRAG</h2>
  <p>Direkt zum Online-Antrag, einfach<br>und schnell</p>
  <svg class="chev" viewBox="0 0 44 40"><path d="M17 9 L28 20 L17 31" fill="none" stroke="#5a7ca6" stroke-width="5"/></svg>
</a>
<a class="abs card" style="left:750px">
  <h2>FINLO REPORT BESTELLEN</h2>
  <p>Unser Report verrät Ihnen die legalen Tricks für Sofortkredite ohne Bonvia.</p>
  <svg class="chev" viewBox="0 0 44 40"><path d="M17 9 L28 20 L17 31" fill="none" stroke="#5a7ca6" stroke-width="5"/></svg>
</a>

<article class="abs intro">
  <h3>Sie benötigen Bargeld und haben keine Chance auf einen Kredit?</h3>
  <p>Finlo-Welt unterstützt Sie bei der Suche nach einem Seriösen Anbieter zu unterstützen. Vielleicht haben Sie ja einen Eintrag bei der Bonvia oder rutschen aus einem anderem Grund durchs Raster.</p>
  <p>Gerade auf solche "Fälle" hat sich Finlo-Welt spezialisiert!</p>
</article>
<a class="teaser" style="top:772px"><span>Ein Trick mit dem Sie das beste Angebot<br>erhalten.</span></a>
<a class="teaser" style="top:840px"><span>Jetzt update: Kredite für Arbeitslose</span></a>
<a class="abs more">mehr lesen<span class="sq"></span></a>

<div class="abs product" role="img" aria-label="Illustration: Report-Verpackung mit steigendem Diagramm und CD"></div>
<div class="adhead abs adhead2"><span class="lbl" style="left:3px;right:auto"><b>Plunko</b>-Anzeigen</span><span style="position:absolute;right:0"><span class="nav"></span><span class="nav on"></span></span></div>
<div class="ad2" style="top:554px"><b>Missbrauch Kreditkarte</b>Bleiben Sie nicht auf dem<br>Schaden sitzen. Jetzt bei<br>Harnoa Direkt absichern!<i>www.HarnoaDirekt.de</i></div>
<div class="ad2" style="top:657px"><b>NEU: Prepaid Kreditkarte</b>Sicher &amp; ohne Bankkonto<br>weltweit zahlen. Alle Infos<br>finden Sie hier!<i>www.quiplakarte.com</i></div>

<div class="abs pillbox">
  <a class="pill" style="top:18px"><span class="go"></span>Alle wichtigen Kredit-Anbieter im Überblick</a>
  <a class="pill" style="top:58px"><span class="go"></span>Kreditkarten für Selbstst./Unternehmer</a>
</div>

<nav class="abs footnav">HOME | LINK | LINK | LINK | LINK</nav>
</body>
</html>
```